Investment Advisor E-Newsletter Banner Design

I need a banner designed for an email newsletter that will be sent monthly to clients and prospects. We want to see designs that are elegant and use our logo well. The banner should be 922x150px and should go well with the www.bhtlwest.com website. Should include Logo and email and phone number.

Target Market(s)

High net worth investors

Number of Pages Required

1 page

Requirements
Must have
• logo, place for email (info@bhtlwest.com) and phone number (555-219-0387), colors and design that work well with www.bhtlwest.com website

```html
<!DOCTYPE html>
<html lang="en">
<head>
<meta charset="utf-8">
<title>Bayhill Trust West – Newsletter Banner</title>
<link rel="stylesheet" href="https://fonts.googleapis.com/css2?family=Montserrat:wght@500;600&display=swap">
<style>
  :root {
    --navy: #2a2a7c;
    --navy-deep: #232370;
    --white: #ffffff;
    --sage: #b9cf8a;
    --leaf: #9cc25a;
    --blush: #e9c9c0;
    --wood: #c8a891;
    --copper: #b08064;
  }
  html, body {
    margin: 0;
    padding: 0;
    overflow: hidden;
    background: var(--white);
  }
  .banner {
    position: relative;
    width: 1200px;
    height: 195px;
    overflow: hidden;
    background: var(--white);
    font-family: "Montserrat", Arial, sans-serif;
  }
  .banner__photo {
    position: absolute;
    top: 0;
    right: 0;
    width: 560px;
    height: 195px;
    background:
      radial-gradient(ellipse at 80% 30%, var(--leaf) 0%, rgba(156,194,90,0) 55%),
      radial-gradient(ellipse at 50% 20%, var(--blush) 0%, rgba(233,201,192,0) 60%),
      linear-gradient(180deg, var(--sage) 0%, var(--blush) 55%, var(--wood) 80%, var(--copper) 100%);
  }
  .banner__photo-fade {
    position: absolute;
    top: 0;
    right: 300px;
    width: 260px;
    height: 195px;
    background: linear-gradient(90deg, var(--white) 0%, rgba(255,255,255,0) 100%);
  }
  .brand {
    position: absolute;
    left: 30px;
    top: 30px;
    display: flex;
    align-items: center;
    gap: 18px;
    color: var(--navy);
    font-weight: 600;
  }
  .brand__dot {
    width: 62px;
    height: 62px;
    border-radius: 50%;
    background: var(--navy);
  }
  .brand__name {
    display: block;
    font-size: 36px;
    line-height: 1.05;
    letter-spacing: 0.2px;
  }
  .brand__tagline {
    display: block;
    margin-top: 10px;
    font-size: 16px;
  }
  .contact-bar {
    position: absolute;
    left: 0;
    top: 146px;
    width: 900px;
    height: 37px;
    background: linear-gradient(90deg, var(--navy-deep) 0%, var(--navy) 70%, rgba(42,42,124,0) 100%);
    display: flex;
    align-items: center;
    padding-left: 29px;
    box-sizing: border-box;
    color: var(--white);
    font-size: 14px;
    font-weight: 500;
    letter-spacing: 0.6px;
  }
  .contact-bar__item {
    display: flex;
    align-items: center;
    gap: 10px;
    margin-right: 30px;
  }
  .contact-bar__icon {
    width: 17px;
    height: 17px;
    fill: none;
    stroke: var(--white);
    stroke-width: 1.4;
  }
</style>
</head>
<body>
  <div class="banner">
    <div class="banner__photo" role="img" aria-label="Stacks of coins rising toward a small model house on a soft green background"></div>
    <div class="banner__photo-fade"></div>

    <div class="brand">
      <div class="brand__dot"></div>
      <div class="brand__text">
        <span class="brand__name">Bayhill Trust</span>
        <span class="brand__tagline">West Advisors, Inc.</span>
      </div>
    </div>

    <div class="contact-bar">
      <div class="contact-bar__item">
        <svg class="contact-bar__icon" viewBox="0 0 24 24" aria-hidden="true">
          <path d="M5 3h4l2 5-2.5 1.5a11 11 0 0 0 6 6L16 13l5 2v4a2 2 0 0 1-2 2A16 16 0 0 1 3 5a2 2 0 0 1 2-2z"/>
        </svg>
        <span>555-219-0387</span>
      </div>
      <div class="contact-bar__item">
        <svg class="contact-bar__icon" viewBox="0 0 24 24" aria-hidden="true">
          <rect x="2" y="5" width="20" height="14"/>
          <path d="M2 5l10 8 10-8"/>
        </svg>
        <span>INFO@BHTLWEST.COM</span>
      </div>
    </div>
  </div>
</body>
</html>
```